Birch & Ember Website Design (Rustic/Western)

OVERVIEW
Birch & Ember Supply House (aka Birch & Ember) manufactures rustic / western furniture and décor for cabins, lodges, and ranches. We also offer a line of accessories to complement our product line.
WEB PAGE (www.BirchAndEmber.example)
We are looking for a new web page design to represent our mountain-style (log furniture) and country-style (barnwood furniture) product line. We would like to re-create our existing homepage with a similar style template for our product line.
Our website is currently under construction – a draft has been published as an example outline. We are currently using Plinkora.example for our online store.
THEME
The overall theme needs to appear rustic, yet elegant. Listed below are only suggestions, not requirements. Please use your own creativity.
* Photographs: We will use our own photographs, for now any photograph will suffice.
* Background Colors: dark brown (rgb 21-9-2), medium brown (rgb 39-17-4), light brown (rgb 72-34-3). White background is also an option.
* Font Colors: beige (rgb 233-164-118), gold (rgb 151-98-2)
• Mountain-Style Images: cabin, wildlife, mountains, fishing, wildlife, trees, etc.
* Mountain-Style Colors: hunter green
* Country-Style Images: western, ranch, barn, farm animals, horse buggies, horseshoes, etc.
* Country-Style Colors: maroon
Thanks to all who are participating.
Target Market(s)
Outdoor enthusiasts who enjoy mountain living or country living. Our primary target market is our local market and within a 100 mile radius of our location.
Industry/Entity Type
Construction
Requirements
Must have
- Rustic, yet elegant design.
Homepage and product template page for displaying each item.
Nice to have
- Source code and functionality is optional.
Mountain-Style theme to represent our collection of log furniture and décor suited for cabins and lodges. Suggested color: hunter green. Images may include cabin, wildlife, mountains, fishing, wildlife, trees, etc.
Country-Style theme to represent our collection of barnwood furniture and décor suited for farms and ranches. Suggested color: maroon. Images may include western, ranch, barn, farm animals, horse buggies, horseshoes, etc.

```html
<!DOCTYPE html>
<html lang="en">
<head>
<meta charset="utf-8">
<title>Birch &amp; Ember Supply House</title>
<link rel="stylesheet" href="https://fonts.googleapis.com/css2?family=Cantarell:wght@400;700&family=Open+Sans:wght@400;600&display=swap">
<style>
:root{
  --page:#3b1b06;
  --nav:#4b2409;
  --panel:#e2e2e2;
  --card:#f2f2f2;
  --card-line:#d4d4d4;
  --heading:#2b2f5a;
  --body:#333;
  --button:#4a2305;
  --button-text:#f0e2d0;
  --footer:#1a0f06;
  --footer-text:#e6ddd2;
  --accent:#e9a476;
  --white:#fff;
}
*{box-sizing:border-box;margin:0;padding:0}
html,body{width:1200px;height:900px;overflow:hidden}
body{background:var(--page);font-family:"Open Sans",sans-serif;color:var(--body);position:relative}
.abs{position:absolute}

/* header */
.header{left:0;top:0;width:1200px;height:72px;background:linear-gradient(90deg,#5a2a0e,#6f3716 50%,#5a2b0f)}
.brand{left:502px;top:14px;width:196px;height:52px;background:#1e1109;border:2px solid #d9c6ac;display:flex;align-items:center;justify-content:center;gap:8px}
.brand-mark{width:10px;height:10px;background:var(--accent)}
.brand-name{font-family:"Cantarell",sans-serif;font-weight:700;font-size:16px;color:var(--accent);letter-spacing:1px}
.social-top{left:905px;top:8px;display:flex;gap:6px}
.social-top span{width:24px;height:14px;border-radius:50%;background:#3d6fb5}
.social-top span:nth-child(3){background:#e2832c}
.social-top span:nth-child(4){background:#6a9a3c}
.search{left:873px;top:42px;width:156px;height:15px;border-bottom:1px solid #c9b9a8}
.search svg{position:absolute;right:4px;top:0}

.nav{left:0;top:72px;width:1200px;height:23px;background:var(--nav);border-top:1px solid #8a5a3a;border-bottom:1px solid #8a5a3a}
.nav a{font-family:"Cantarell",sans-serif;font-size:10px;color:#e6dccf;text-decoration:none;text-transform:uppercase;line-height:20px;position:absolute}

/* hero */
.hero{left:172px;top:95px;width:858px;height:188px;background:linear-gradient(180deg,#9eb0c0,#557034)}
.hero-caption{left:172px;top:262px;width:858px;height:21px;background:rgba(60,28,8,.7);color:#f0e6d8;font-family:"Cantarell",sans-serif;font-size:11px;padding:4px 14px}
.dots{left:945px;top:269px;display:flex;gap:2px}
.dots span{width:8px;height:8px;border-radius:50%;background:#fff}

/* main panel */
.sheet{left:172px;top:283px;width:858px;height:537px;background:var(--white)}
.panel{left:187px;top:287px;width:823px;height:533px;background:var(--panel)}

.side-box{left:196px;width:200px;background:var(--card);border:1px solid var(--card-line)}
.box-title{font-family:"Cantarell",sans-serif;font-size:11px;color:var(--heading);text-transform:uppercase;height:20px;line-height:19px;padding-left:8px;border-bottom:1px solid var(--card-line)}
.side-list li{list-style:none;font-size:7.5px;height:12.4px;line-height:11.4px;padding-left:26px;border-bottom:1px solid var(--card-line);position:relative}
.side-list li:last-child{border-bottom:0}
.side-list li::before{content:"";position:absolute;left:8px;top:3.5px;width:5px;height:5px;border-radius:50%;border:1px solid #999}
.login-form{padding:10px 16px 6px;font-size:7.5px;line-height:9px}
.login-form label{display:block;margin-top:2px}
.login-form .field{width:122px;height:7px;border:1px solid #aaa;background:#fff;margin-bottom:3px}
.remember{display:flex;align-items:center;gap:8px;margin:3px 0 4px}
.remember i{width:7px;height:7px;border:1px solid #999;background:#fff}
.login-btn{display:inline-block;font-size:7.5px;line-height:9px;padding:0 10px;border:1px solid #999;background:#e6e6e6}

.article{left:411px;width:589px;background:var(--card);border:1px solid var(--card-line)}
.article-title{font-family:"Cantarell",sans-serif;font-size:11px;font-weight:400;color:var(--heading);height:20px;line-height:20px;padding-left:12px;border-bottom:1px solid var(--card-line);background:linear-gradient(#fafafa,#ececec)}
.article-text{position:absolute;left:14px;top:22px;width:254px;font-size:7.5px;line-height:7.6px;letter-spacing:.45px}
.article-text p{margin-bottom:3px}
.read-more{position:absolute;left:10px;width:135px;height:12px;background:var(--button);color:var(--button-text);font-family:"Cantarell",sans-serif;font-size:8.5px;text-align:center;line-height:12px}
.article-photo{position:absolute;left:300px;width:266px;padding:5px 7px;background:#e4e4e4;box-shadow:0 1px 2px rgba(0,0,0,.3)}
.article-photo div{height:57px}

.category{top:729px;width:188px;height:76px;background:var(--card)}
.category h3{font-family:"Cantarell",sans-serif;font-weight:400;font-size:11px;color:var(--heading);text-align:center;text-transform:uppercase;height:17px;line-height:18px}
.category div{height:59px}

/* footer */
.footer{left:172px;top:820px;width:858px;height:80px;background:var(--footer);color:var(--footer-text);font-size:7.5px;line-height:8.6px;letter-spacing:.3px}
.footer-contact{position:absolute;left:25px;top:11px}
.footer-contact p+p{margin-top:8px}
.social-foot{position:absolute;right:30px;top:23px;display:flex;gap:3px}
.social-foot span{width:26px;height:13px;background:#3d6fb5}
.social-foot span:nth-child(3){background:#6a9a3c}
.social-foot span:nth-child(4){background:#2a72a8}
.copyright{position:absolute;right:28px;top:46px;text-align:right}
</style>
</head>
<body>

<header class="abs header"></header>
<div class="abs brand"><span class="brand-mark"></span><span class="brand-name">BIRCH &amp; EMBER</span></div>
<div class="abs social-top" aria-label="Social links"><span></span><span></span><span></span><span></span></div>
<div class="abs search">
  <svg width="14" height="14" viewBox="0 0 14 14"><circle cx="6" cy="6" r="4.2" fill="none" stroke="#fff" stroke-width="1.6"/><line x1="9" y1="9" x2="13" y2="13" stroke="#fff" stroke-width="1.8"/></svg>
</div>

<nav class="abs nav">
  <a style="left:200px">Home</a>
  <a style="left:298px">Office / Bar Room</a>
  <a style="left:484px">Accessories</a>
  <a style="left:628px">Bargain Corner</a>
  <a style="left:801px">About Us</a>
  <a style="left:925px">Contact Us</a>
</nav>

<div class="abs hero" role="img" aria-label="Photo: mountain landscape with rock outcrop and wildflower meadow"></div>
<div class="abs hero-caption">Birch &amp; Ember</div>
<div class="abs dots"><span></span><span></span><span></span></div>

<div class="abs sheet"></div>
<div class="abs panel"></div>

<aside>
  <section class="abs side-box" style="top:292px">
    <h2 class="box-title">About B&amp;E</h2>
    <ul class="side-list"><li>Lorem Ipsum is simply</li><li>Lorem Ipsum is simply</li><li>Lorem Ipsum is simply</li><li>Lorem Ipsum is simply</li></ul>
  </section>
  <section class="abs side-box" style="top:366px">
    <h2 class="box-title">Western Furniture</h2>
    <ul class="side-list"><li>Lorem Ipsum is simply</li><li>Lorem Ipsum is simply</li><li>Lorem Ipsum is simply</li></ul>
  </section>
  <section class="abs side-box" style="top:428px">
    <h2 class="box-title">Login</h2>
    <div class="login-form">
      <label>User Name</label><div class="field"></div>
      <label>Password</label><div class="field"></div>
      <div class="remember">Remember Me <i></i></div>
      <span class="login-btn">Log in</span>
    </div>
    <ul class="side-list"><li>Forget your password ?</li><li>Forget your username ?</li><li>Create an account</li></ul>
  </section>
</aside>

<main>
  <article class="abs article" style="top:292px;height:108px">
    <h2 class="article-title">LOREM IPSUM</h2>
    <div class="article-text"><p>Lorem Ipsum is simply dummy text of the printing and typesetting industry. Lorem Ipsum has been the industry's standard dummy text ever since the 1500</p><p>Contrary to popular belief, Lorem Ipsum is not simply random text. It has roots in a piece of classical Latin literature from 45 BC, making it over 2000 years old</p></div>
    <div class="read-more" style="top:87px">READ MORE</div>
    <div class="article-photo" style="top:26px"><div role="img" aria-label="Photo: bare forest trees" style="background:#41648f"></div></div>
  </article>
  <article class="abs article" style="top:405px;height:100px">
    <h2 class="article-title">LOREM IPSUM</h2>
    <div class="article-text"><p>Lorem Ipsum is simply dummy text of the printing and typesetting industry. Lorem Ipsum has been the industry's standard dummy text ever since the 1500</p><p>Contrary to popular belief, Lorem Ipsum is not simply random text.</p></div>
    <div class="read-more" style="top:76px">READ MORE</div>
    <div class="article-photo" style="top:24px"><div role="img" aria-label="Photo: barnwood bench table" style="background:#a9774c"></div></div>
  </article>
  <article class="abs article" style="top:512px;height:98px">
    <h2 class="article-title">LOREM IPSUM</h2>
    <div class="article-text"><p>Lorem Ipsum is simply dummy text of the printing and typesetting industry. Lorem Ipsum has been the industry's standard dummy text ever since the 1500</p><p>Contrary to popular belief, Lorem Ipsum is not simply random text. It has roots in</p></div>
    <div class="read-more" style="top:75px">READ MORE</div>
    <div class="article-photo" style="top:23px"><div role="img" aria-label="Photo: log bed frame on a lawn" style="background:#5f7f38"></div></div>
  </article>
  <article class="abs article" style="top:618px;height:98px">
    <h2 class="article-title">LOREM IPSUM</h2>
    <div class="article-text"><p>Lorem Ipsum is simply dummy text of the printing and typesetting industry. Lorem Ipsum has been the industry's standard dummy text ever since the 1500</p><p>Contrary to popular belief, Lorem Ipsum is not simply random text. It has roots in a piece of</p></div>
    <div class="read-more" style="top:75px">READ MORE</div>
    <div class="article-photo" style="top:24px"><div role="img" aria-label="Photo: wooden planter boxes with flowers" style="background:#8e7860"></div></div>
  </article>

  <section class="abs category" style="left:196px"><h3>Lighting</h3><div role="img" aria-label="Photo: pair of rustic table lamps" style="background:#a5785a"></div></section>
  <section class="abs category" style="left:401px"><h3>Wall Décor</h3><div role="img" aria-label="Photo: horseshoe wall hanging on barnwood" style="background:#6f6a62"></div></section>
  <section class="abs category" style="left:606px"><h3>Fine Art Gallery</h3><div role="img" aria-label="Photo: evening sky over the horizon" style="background:#161832"></div></section>
  <section class="abs category" style="left:811px"><h3>Accessories</h3><div role="img" aria-label="Photo: rustic accessories on a wooden table" style="background:#7a5238"></div></section>
</main>

<footer class="abs footer">
  <div class="footer-contact">
    <p>Birch &amp; Ember Supply House<br>Cedar Hollow, MT 59000</p>
    <p>Phone: (406) 555-0172<br>Email: hello@birchandember.example<br>Website: www.BirchAndEmber.example</p>
  </div>
  <div class="social-foot" aria-label="Social links"><span></span><span></span><span></span><span></span></div>
  <div class="copyright">© 2014 Copyright<br>Birch &amp; Ember Supply House All Rights Reserved.</div>
</footer>

</body>
</html>
```